Logo and Business Card Design

Harbor Crest Logistics provides our customers with one call solutions to packing, trucking and warehousing needs throughout the supply chain.
We need ideas for a logo/business card. I have 2 general concepts.
1. Modern logo involving: the globe, Harbor Crest, arrow, movement, the two words having 2 different fonts/colors, the number 1.
2. Logo involving Lion/Winged Lion: incorporate lion onto globe, tagline "First in Every Freight", Always, Onward.

Target Market(s)

International Logistics companies, Air cargo companies, manufacturing companies

Industry/Entity Type

Business

Contact Information for Business Card

Dale Verhoeven
Owner
Harbor Crest Logistics
2874 Wexley Blvd.
Maple Ridge Falls, WI 60219
555-308-2946
daleh@harborcrestfreight.example

Font styles to use
Sans Serif

Requirements
Must have
• 1. Modern logo involving: the globe, Harbor Crest, arrow, movement, the two words having 2 different fonts/colors, the number 1.
Nice to have
Should not have
• Do not have too complex of a design.

```html
<!DOCTYPE html>
<html lang="en">
<head>
<meta charset="utf-8">
<title>Harbor Crest Logistics — Business Card</title>
<link rel="stylesheet" href="https://fonts.googleapis.com/css2?family=Open+Sans:wght@400;600;700&family=Michroma&display=swap">
<style>
  :root {
    --backdrop: #d6d6d6;
    --card-white: #ffffff;
    --brand-blue: #2d43a0;
    --band-light: #2f86d6;
    --band-dark: #1d3f9a;
    --ink: #1a1a1a;
    --night: #0b0d10;
    --night-soft: #1c2128;
    --text-light: #f4f4f4;
    --rule: #2a2a2a;
  }
  * { box-sizing: border-box; margin: 0; padding: 0; }
  html, body {
    width: 1200px; height: 900px; overflow: hidden;
    background: var(--backdrop);
  }
  .card {
    position: absolute; left: 100px; top: 150px;
    width: 1000px; height: 600px;
    border-radius: 40px; overflow: hidden;
    background: var(--card-white);
    box-shadow: 0 18px 40px rgba(0,0,0,0.25);
  }
  .card-top { position: absolute; inset: 0 0 auto 0; height: 275px; }
  .brand-mark {
    position: absolute; left: 60px; top: 40px;
    width: 200px; height: 200px; border-radius: 50%;
    background: radial-gradient(circle at 40% 35%, #8fc6ee, #2f6fb8 70%, #1f3f8a);
  }
  .brand-name {
    position: absolute; left: 300px; top: 88px;
    font-family: "Open Sans", sans-serif; font-weight: 700;
    font-size: 46px; color: var(--brand-blue); white-space: nowrap;
  }
  .brand-rule {
    position: absolute; left: 300px; top: 160px;
    width: 510px; height: 2px; background: var(--rule);
  }
  .tagline {
    position: absolute; left: 302px; top: 176px;
    font-family: "Michroma", sans-serif; font-size: 19px;
    letter-spacing: 13px; color: var(--ink); white-space: nowrap;
  }
  .motion-band {
    position: absolute; left: 0; right: 0; top: 275px; height: 26px;
    background: linear-gradient(90deg, var(--band-dark), var(--band-light) 60%, var(--band-dark));
    display: flex; align-items: center; justify-content: center;
    overflow: hidden;
  }
  .motion-band span {
    font-family: "Michroma", sans-serif; font-size: 15px;
    letter-spacing: 34px; color: var(--ink); padding-left: 34px; white-space: nowrap;
  }
  .card-bottom {
    position: absolute; left: 0; right: 0; top: 301px; bottom: 0;
    background: linear-gradient(180deg, var(--night) 0%, var(--night-soft) 55%, var(--night) 100%);
    padding: 26px 60px; color: var(--text-light);
    font-family: "Open Sans", sans-serif;
  }
  .person-name { font-size: 30px; font-weight: 700; color: var(--brand-blue); line-height: 1.2; }
  .person-role { font-size: 24px; margin-top: 2px; line-height: 1.3; }
  .contact-list { list-style: none; margin-top: 40px; font-size: 24px; line-height: 34px; }
  .contact-list li { display: flex; align-items: flex-start; gap: 10px; }
  .contact-icon { width: 30px; height: 30px; flex: none; margin-top: 3px; fill: var(--brand-blue); }
</style>
</head>
<body>
  <article class="card">
    <header class="card-top">
      <div class="brand-mark" role="img" aria-label="Globe emblem area"></div>
      <div class="brand-name">Harbor Crest Logistics</div>
      <div class="brand-rule"></div>
      <div class="tagline">FIRST IN EVERY FREIGHT</div>
    </header>
    <div class="motion-band"><span>ALWAYS, ONWARD</span></div>
    <section class="card-bottom">
      <h1 class="person-name">Dale Verhoeven</h1>
      <p class="person-role">Owner</p>
      <ul class="contact-list">
        <li>
          <svg class="contact-icon" viewBox="0 0 24 24" aria-hidden="true"><path d="M6.6 10.8a15.1 15.1 0 0 0 6.6 6.6l2.2-2.2a1 1 0 0 1 1-.25 11.4 11.4 0 0 0 3.6.57 1 1 0 0 1 1 1V20a1 1 0 0 1-1 1A17 17 0 0 1 3 4a1 1 0 0 1 1-1h3.5a1 1 0 0 1 1 1c0 1.25.2 2.45.57 3.57a1 1 0 0 1-.25 1z"/></svg>
          <span>555-308-2946</span>
        </li>
        <li>
          <svg class="contact-icon" viewBox="0 0 24 24" aria-hidden="true"><path d="M3 6h18v12H3z M3 6l9 7 9-7" fill="none" stroke="#2d43a0" stroke-width="2"/></svg>
          <span>daleh@harborcrestfreight.example</span>
        </li>
        <li>
          <svg class="contact-icon" viewBox="0 0 24 24" aria-hidden="true"><path d="M12 3l10 9h-3v8h-5v-6h-4v6H5v-8H2z"/></svg>
          <span>Harbor Crest Logistics 2874 Wexley Blvd. Maple<br>Ridge Falls, WI 60219</span>
        </li>
      </ul>
    </section>
  </article>
</body>
</html>
```